Business cards and stationary design

We just completed the design of our new logo and we need to print new business cards and letterhead for our nonprofit. We are looking for a fresh new design that shows off our new logo. On letterhead, we must have a column on the right or left to include our Board of Directors (up to 45 names) (see attachment)

Industry/Entity Type

Non-Profit

Contact Information for Business Card

Standard business card with name, title, Company name, mailing address phone numbers, email address and website. Tagline on back "Bringing the homeless home"

Font styles to use
Sans Serif

Requirements
Must have
• include pertinent information above
• new logo
• fonts compatible with logo
• should use logo colors only
Nice to have
• tag lines

```html
<!DOCTYPE html>
<html lang="en">
<head>
<meta charset="utf-8">
<title>Hearth Circle – Business Card</title>
<link href="https://fonts.googleapis.com/css2?family=Michroma&family=Gelasio:wght@400&display=swap" rel="stylesheet">
<style>
  :root {
    --teal: #0a82a0;
    --sun: #fbb52b;
    --red: #e8202a;
    --ink: #3a3a3a;
    --paper: #ffffff;
    --sky-edge: #8fbdd3;
    --sky-center: #ffffff;
    --backdrop: #e6e7e9;
  }
  * { margin: 0; padding: 0; box-sizing: border-box; }
  html, body { width: 1200px; height: 1200px; overflow: hidden; }
  body {
    background: var(--backdrop);
    display: flex;
    flex-direction: column;
    align-items: center;
    justify-content: center;
    gap: 60px;
  }
  .card {
    width: 700px;
    height: 400px;
    position: relative;
    overflow: hidden;
    box-shadow: 0 6px 18px rgba(0,0,0,0.18);
  }

  /* Back side */
  .card-back {
    background: radial-gradient(ellipse at 50% 50%, var(--sky-center) 0%, #e3eff6 35%, var(--sky-edge) 100%);
    display: flex;
    align-items: center;
    justify-content: center;
  }
  .tagline {
    font-family: "Michroma", sans-serif;
    font-variant: small-caps;
    font-weight: 400;
    color: var(--teal);
    font-size: 30px;
    line-height: 1.35;
    letter-spacing: 2px;
    text-align: center;
  }
  .tagline-line { display: flex; align-items: center; gap: 8px; }
  .tagline-line::before, .tagline-line::after {
    content: ""; height: 1.5px; background: var(--teal); width: 70px;
  }
  .tagline-line.first::after { visibility: hidden; }
  .tagline-line.second::before { visibility: hidden; }

  /* Front side */
  .card-front { background: var(--paper); }
  .person {
    position: absolute; left: 58px; top: 62px;
  }
  .person-name {
    font-family: "Michroma", sans-serif;
    font-weight: 400;
    color: var(--teal);
    font-size: 22px;
    letter-spacing: 5px;
    text-transform: uppercase;
  }
  .person-title {
    font-family: "Gelasio", serif;
    color: var(--ink);
    font-size: 20px;
    margin-top: 4px;
  }
  .contact-list {
    position: absolute; left: 58px; top: 170px;
    list-style: none;
    font-family: "Gelasio", serif;
    color: var(--ink);
    font-size: 19px;
  }
  .contact-list li { display: flex; align-items: center; gap: 10px; line-height: 28px; }
  .contact-icon { width: 20px; height: 20px; flex: none; }
  .contact-list .address { margin-top: 30px; align-items: flex-start; }
  .address .contact-icon { margin-top: 4px; }

  .brand {
    position: absolute; right: 46px; top: 50%;
    transform: translateY(-50%);
    width: 250px;
    display: flex; flex-direction: column; align-items: center; gap: 16px;
  }
  .brand-mark { width: 34px; height: 34px; background: var(--sun); }
  .brand-name {
    font-family: "Michroma", sans-serif;
    color: var(--teal);
    font-size: 24px;
    letter-spacing: 3px;
    text-align: center;
    line-height: 1.3;
  }
</style>
</head>
<body>

  <section class="card card-back" aria-label="Card back">
    <h2 class="tagline">
      <span class="tagline-line first">Bringing the</span>
      <span class="tagline-line second">homeless home</span>
    </h2>
  </section>

  <section class="card card-front" aria-label="Card front">
    <div class="person">
      <h1 class="person-name">Marcus Delaney</h1>
      <p class="person-title">Chairman</p>
    </div>

    <ul class="contact-list">
      <li>
        <svg class="contact-icon" viewBox="0 0 20 20" aria-hidden="true"><circle cx="10" cy="10" r="10" fill="var(--teal)"/><path d="M7 5.5l1.6 0 .8 2.4-1.1.8a6 6 0 0 0 3 3l.8-1.1 2.4.8v1.6c0 .6-.5 1-1.1 1A8 8 0 0 1 6 6.6c0-.6.4-1.1 1-1.1z" fill="#fff"/></svg>
        555.010.4821
      </li>
      <li>
        <svg class="contact-icon" viewBox="0 0 20 20" aria-hidden="true"><circle cx="10" cy="10" r="10" fill="var(--teal)"/><g fill="none" stroke="#fff" stroke-width="1.1"><circle cx="10" cy="10" r="5"/><ellipse cx="10" cy="10" rx="2.2" ry="5"/><path d="M5 10h10"/></g></svg>
        www.hearthcircle.org
      </li>
      <li>
        <svg class="contact-icon" viewBox="0 0 20 20" aria-hidden="true"><circle cx="10" cy="10" r="10" fill="var(--teal)"/><rect x="5" y="6.5" width="10" height="7" fill="#fff"/><path d="M5 6.5l5 4 5-4" fill="none" stroke="var(--teal)" stroke-width="1"/></svg>
        marcus@hearthcircle.org
      </li>
      <li class="address">
        <svg class="contact-icon" viewBox="0 0 20 20" aria-hidden="true"><circle cx="10" cy="10" r="10" fill="var(--teal)"/><path d="M10 4.5a3.8 3.8 0 0 0-3.8 3.8c0 2.8 3.8 7 3.8 7s3.8-4.2 3.8-7A3.8 3.8 0 0 0 10 4.5z" fill="#fff"/><circle cx="10" cy="8.3" r="1.4" fill="var(--teal)"/></svg>
        <span>P.O Box 402318<br>Dallas, Texas 75230</span>
      </li>
    </ul>

    <div class="brand">
      <span class="brand-mark" aria-hidden="true"></span>
      <p class="brand-name">Hearth<br>Circle</p>
    </div>
  </section>

</body>
</html>
```